pipequell new business sales flyer

this is a flyer to tell people what pipequell does and what is great about the service we offer.

please see attached doc for brief, and add the contact details below.

12/18-26 Wexbury Rd, Altona North VIC 3025
03 9461 2078
0428 716 304
bookings@pipequell.com.au
www.pipequell.com.au

Target Market(s)

home builder companies

Industry/Entity Type

residential home building construction

Colors
0054AA
0677BA
7BADD7
CADEEF
E8F1F8
0094D4
00A9DD
6FCCEA
C7EBF8
E9F6FB
FFC000
F8CF3A
FAE287
FDF2CF
FEFAEE

Requirements
Must have
• logo/images/

```html
<!DOCTYPE html>
<html lang="en">
<head>
<meta charset="utf-8">
<title>pipequell – sales flyer</title>
<link rel="stylesheet" href="https://fonts.googleapis.com/css2?family=Oswald:wght@500;600&family=Poppins:wght@400;600;700;800&display=swap">
<style>
  :root{
    --navy:#233f8c;
    --cyan:#00b2de;
    --white:#ffffff;
    --ink:#1e1e24;
    --backdrop:#808080;
    --brick:#8e4a42;
    --brick-dark:#5e302c;
  }
  *{box-sizing:border-box;margin:0;padding:0}
  html,body{width:1200px;height:851px;overflow:hidden}
  body{background:var(--backdrop);position:relative;font-family:"Poppins",sans-serif;color:var(--ink)}
  .page{position:absolute;top:73px;width:486px;height:687px;background:var(--white);overflow:hidden}
  .page--front{left:98px}
  .page--back{left:616px}

  .hero-photo{position:absolute;left:0;top:0;width:486px;height:300px}

  .brand{position:absolute;left:0;width:100%;text-align:center}
  .brand__name{font-family:"Poppins",sans-serif;font-weight:800;color:var(--navy);letter-spacing:-2px;line-height:1;display:inline-flex;align-items:center;gap:8px}
  .brand__dot{display:inline-block;border-radius:50%;background:var(--cyan)}
  .brand__tag{font-family:"Poppins",sans-serif;font-weight:700;color:var(--cyan);letter-spacing:.6px;line-height:1}
  .page--front .brand{top:310px}
  .page--front .brand__name{font-size:62px}
  .page--front .brand__dot{width:16px;height:16px;margin-top:26px}
  .page--front .brand__tag{font-size:10.5px;margin-top:4px}
  .page--back .brand{top:18px}
  .page--back .brand__name{font-size:52px}
  .page--back .brand__dot{width:14px;height:14px;margin-top:22px}
  .page--back .brand__tag{font-size:8.6px;margin-top:3px}

  .section-title{position:absolute;height:30px;background:var(--navy);color:var(--white);font-family:"Oswald",sans-serif;font-weight:500;font-size:19.5px;line-height:30px;padding-left:16px}
  .section-title__dot{position:absolute;top:4px;width:22px;height:22px;border-radius:50%;background:var(--cyan)}
  .page--front .section-title{left:42px;top:414px;width:416px}
  .page--front .section-title__dot{left:-14px}
  .page--back .section-title{left:54px;top:95px;width:405px;padding-left:5px}
  .page--back .section-title__dot{left:-26px}

  .copy{position:absolute;font-size:9.6px;line-height:12.7px;text-align:justify}
  .copy p+p{margin-top:12.7px}
  .page--front .copy{left:57px;top:457px;width:401px}
  .page--back .copy{left:33px;top:141px;width:424px}

  .highlights{position:absolute;left:34px;top:259px;width:422px;height:127px;background:var(--cyan);border-radius:8px;padding:15px 18px 0 37px;list-style:none;color:var(--white);font-weight:700;font-size:10.8px;line-height:13.6px}
  .highlights::before{content:"";position:absolute;left:26px;top:26px;width:1px;height:90px;background:var(--white)}
  .highlights li{position:relative;margin-bottom:11px}
  .highlights li svg{position:absolute;left:-22px;top:0;width:13px;height:13px;background:var(--cyan)}

  .gallery{position:absolute;left:34px;top:398px;display:flex;gap:4px}
  .gallery__tile{width:138px;height:136px;border:1px solid #9a9a9a;position:relative}
  .gallery__tile--pipe{background:radial-gradient(circle at 42% 30%,#1a140c 0,#4a3a22 22%,#b89a66 55%,#efe2b8 100%)}
  .gallery__tile--crack{background:linear-gradient(160deg,#f2f2f0,#dcdcd8)}
  .gallery__tile--camera{background:radial-gradient(circle at 60% 35%,#5f6648 0,#9aa37d 45%,#cfd6b4 100%)}
  .gallery__caption{position:absolute;left:10px;top:58px;color:var(--white);font-weight:600;font-size:15px;line-height:15px;letter-spacing:-.3px}

  .service-line{position:absolute;left:0;top:555px;width:100%;text-align:center;font-weight:700;font-size:16.5px;color:var(--navy)}
  .service-line span{color:var(--cyan)}

  .footer-wave{position:absolute;left:0;width:486px}
  .page--front .footer-wave{top:577px;height:110px}
  .page--back .footer-wave{top:545px;height:142px}

  .contact{position:absolute;left:0;width:100%;display:flex;justify-content:center;align-items:center;gap:7px;color:var(--white);font-family:"Oswald",sans-serif;font-weight:500;font-size:22px;line-height:1}
  .page--front .contact{top:638px}
  .page--back .contact{top:646px}
  .contact svg{width:20px;height:20px;flex:none}
  .contact__gap{width:4px}
</style>
</head>
<body>

<section class="page page--front">
  <svg class="hero-photo" viewBox="0 0 486 300" role="img" aria-label="Photo of a brick wall with a stepped crack caused by slab heave">
    <defs>
      <linearGradient id="brickTone" x1="0" y1="0" x2="1" y2="1">
        <stop offset="0" stop-color="#7d3f39"/>
        <stop offset=".5" stop-color="#9a564b"/>
        <stop offset="1" stop-color="#6e3a34"/>
      </linearGradient>
    </defs>
    <path d="M0 0H486V136C430 230 330 280 230 279C130 278 50 240 0 186Z" fill="url(#brickTone)"/>
    <path d="M0 190C60 242 150 287 285 284C160 293 60 264 0 214Z" fill="var(--cyan)"/>
  </svg>

  <div class="brand">
    <div class="brand__name">pipequell<span class="brand__dot"></span></div>
    <div class="brand__tag">DRAINAGE &amp; PLUMBING SOLUTIONS</div>
  </div>

  <h2 class="section-title"><span class="section-title__dot"></span>What is slab heave costing your business?</h2>

  <div class="copy">
    <p>The SBA (State Building Authority) put out a report regarding the growing concern of slab heave in new homes. One of their recommendations to eliminate the problem is to conduct an independent inspection (rather than self-certification) of installed stormwater drainage systems. This should be an extension of mandatory inspections for building structures.</p>
    <p>Pipequell are the only specialized drainage inspectors to offer a cost-effective independent solution to inspect drains on each site. We are saving our home builder clients a lot of money. Talk to us today about how.</p>
  </div>

  <svg class="footer-wave" viewBox="0 0 486 110" preserveAspectRatio="none" aria-hidden="true">
    <path d="M150 18C290 -4 410 20 486 58V70C400 32 300 10 150 21Z" fill="var(--cyan)"/>
    <path d="M0 84C120 22 300 12 486 82V110H0Z" fill="var(--navy)"/>
  </svg>

  <div class="contact">
    <svg viewBox="0 0 24 24" fill="none" stroke="var(--cyan)" stroke-width="1.8" aria-hidden="true"><path d="M5 3h4l2 5-3 2a12 12 0 0 0 6 6l2-3 5 2v4a2 2 0 0 1-2 2A17 17 0 0 1 3 5a2 2 0 0 1 2-2z"/></svg>
    <span>03 9461 2078</span>
    <span class="contact__gap"></span>
    <svg viewBox="0 0 24 24" aria-hidden="true"><circle cx="12" cy="12" r="11" fill="var(--cyan)"/><path d="M12 1v22M1 12h22M4 6c5 3 11 3 16 0M4 18c5-3 11-3 16 0" stroke="var(--navy)" stroke-width="1.3" fill="none"/></svg>
    <span>PIPEQUELL.COM.AU</span>
  </div>
</section>

<section class="page page--back">
  <div class="brand">
    <div class="brand__name">pipequell<span class="brand__dot"></span></div>
    <div class="brand__tag">DRAINAGE &amp; PLUMBING SOLUTIONS</div>
  </div>

  <h2 class="section-title"><span class="section-title__dot"></span>Pipequell &nbsp;what we do?</h2>

  <div class="copy">
    <p>Long-term sewer &amp; stormwater damage on new home builds is hitting builders where it hurts, it severely impacts both your reputation and your bank balance. We've got the solution!</p>
    <p>Our fixed-price Drainage Inspection Package catches issues before homeowners move in. Our Post-Slab &amp; Pre Settlement Drain Inspection on every build, sees repairs fixed on the spot, all included in the one low fixed-price. You'll receive a comprehensive report &amp; video footage for each inspection. We pride ourselves on our reputation, customer service is at the forefront of everything we do.</p>
  </div>

  <ul class="highlights">
    <li><svg viewBox="0 0 16 16" fill="none" stroke="#fff" stroke-width="1.6" aria-hidden="true"><circle cx="8" cy="8" r="6.5"/><path d="M5 8l2 2 5-5"/></svg>We have the capacity to take on the largest volume builders!</li>
    <li><svg viewBox="0 0 16 16" fill="none" stroke="#fff" stroke-width="1.6" aria-hidden="true"><circle cx="8" cy="8" r="6.5"/><path d="M5 8l2 2 5-5"/></svg>With over 50,000 jobs under our belt, we know a thing or two about drainage problems.</li>
    <li><svg viewBox="0 0 16 16" fill="none" stroke="#fff" stroke-width="1.6" aria-hidden="true"><circle cx="8" cy="8" r="6.5"/><path d="M5 8l2 2 5-5"/></svg>Did you know? From the homes we've inspected every second home built has on average 2 breaks in the storm water.</li>
  </ul>

  <div class="gallery">
    <div class="gallery__tile gallery__tile--pipe" role="img" aria-label="Camera view inside a stormwater pipe with debris"></div>
    <div class="gallery__tile gallery__tile--crack" role="img" aria-label="Crack running down a white plaster wall"></div>
    <div class="gallery__tile gallery__tile--camera" role="img" aria-label="Drain inspection camera inside a pipe">
      <span class="gallery__caption">cctv<br>inspections<br>and reporting</span>
    </div>
  </div>

  <p class="service-line">CCTV Drain <span>Inspection+ Repairs</span></p>

  <svg class="footer-wave" viewBox="0 0 486 142" preserveAspectRatio="none" aria-hidden="true">
    <path d="M0 4C100 64 220 84 360 74C220 92 90 70 0 22Z" fill="var(--cyan)"/>
    <path d="M0 30C120 92 300 96 486 26V142H0Z" fill="var(--navy)"/>
  </svg>

  <div class="contact">
    <svg viewBox="0 0 24 24" fill="none" stroke="var(--cyan)" stroke-width="1.8" aria-hidden="true"><path d="M5 3h4l2 5-3 2a12 12 0 0 0 6 6l2-3 5 2v4a2 2 0 0 1-2 2A17 17 0 0 1 3 5a2 2 0 0 1 2-2z"/></svg>
    <span>03 9461 2078</span>
    <span class="contact__gap"></span>
    <svg viewBox="0 0 24 24" aria-hidden="true"><circle cx="12" cy="12" r="11" fill="var(--cyan)"/><path d="M12 1v22M1 12h22M4 6c5 3 11 3 16 0M4 18c5-3 11-3 16 0" stroke="var(--navy)" stroke-width="1.3" fill="none"/></svg>
    <span>PIPEQUELL.COM.AU</span>
  </div>
</section>

</body>
</html>
```